Word Page Templates x 5

1 x Letterhead Template with Header and Footer able to be printed to paper and pdf with non blurry resolution
- File attached looks ok on computer screen but does not print the same
- We are wanting it to print like it looks on the screen
- We are wanting it to print not fuzzy in resolution
- We are wanting the banner to be on the absolute edge of the page like it is on the computer screen
- We are needing to print this to paper and pdf with perfect resolution and colour

Please can someone help us!!

I have provided the logo files in our posession. If better resolutions are required please let us know.

We are also wanting 4 simple page templates to be setup in Landscape and Portrait orientation as well once we are happy with the letterhead that is provided samples have been provided
Updates

Hi all I have the vector files available now along with a Colour profile

Requirements
Must have
• Clear when printed on A4 Paper
Should not have
• Blurry images, Colour must be correct (same as Logo) - Please reference our website if need be ..... vornal.com.au

```html
<!DOCTYPE html>
<html lang="en">
<head>
<meta charset="utf-8">
<title>Vornal Pavement Services – Letterhead Templates</title>
<link rel="stylesheet" href="https://fonts.googleapis.com/css2?family=Montserrat:wght@600;800&display=swap">
<style>
  :root {
    --backdrop: #c6c6c6;
    --paper: #ffffff;
    --edge: #2e2e2e;
    --brand-green: #0f8a45;
    --brand-teal: #1d5f62;
    --brand-blue: #263f8e;
    --tagline: #5a6b7a;
  }
  html, body {
    margin: 0;
    padding: 0;
    width: 1069px;
    height: 1200px;
    overflow: hidden;
    background: var(--backdrop);
    font-family: "Montserrat", Arial, sans-serif;
  }
  .sheet {
    position: absolute;
    background: var(--paper);
    border: 1.5px solid var(--edge);
    box-shadow: 0 0 6px rgba(0,0,0,0.45);
    box-sizing: border-box;
    overflow: hidden;
  }
  .sheet--portrait { left: 306px; top: 33px; width: 457px; height: 646px; }
  .sheet--landscape { left: 211px; top: 709px; width: 647px; height: 457px; }

  .footer-band {
    position: absolute;
    left: 0;
    right: 0;
    bottom: 2px;
    height: 6px;
    background: linear-gradient(90deg, var(--brand-green) 0%, var(--brand-green) 45%, var(--brand-teal) 75%, var(--brand-blue) 100%);
  }
  .brand-block {
    position: absolute;
    text-align: right;
    line-height: 1;
  }
  .brand-name {
    display: block;
    font-weight: 800;
    color: var(--brand-teal);
    letter-spacing: 0.5px;
  }
  .brand-tagline {
    display: block;
    font-weight: 600;
    color: var(--tagline);
    letter-spacing: 0.3px;
    margin-top: 2px;
  }
  .brand-square {
    position: absolute;
    background: var(--brand-teal);
  }

  .sheet--portrait .brand-block { right: 19px; bottom: 29px; }
  .sheet--portrait .brand-name { font-size: 14px; }
  .sheet--portrait .brand-tagline { font-size: 3.6px; }
  .sheet--portrait .brand-square { right: 0; bottom: 40px; width: 12px; height: 12px; }

  .sheet--landscape .brand-block { right: 22px; bottom: 36px; }
  .sheet--landscape .brand-name { font-size: 15px; }
  .sheet--landscape .brand-tagline { font-size: 3.8px; }
  .sheet--landscape .brand-square { right: 0; bottom: 48px; width: 13px; height: 13px; }
</style>
</head>
<body>

<section class="sheet sheet--portrait" aria-label="Portrait letterhead">
  <div class="brand-block">
    <span class="brand-name">VORNAL</span>
    <span class="brand-tagline">PAVEMENT SERVICES</span>
  </div>
  <span class="brand-square" aria-hidden="true"></span>
  <div class="footer-band" aria-hidden="true"></div>
</section>

<section class="sheet sheet--landscape" aria-label="Landscape letterhead">
  <div class="brand-block">
    <span class="brand-name">VORNAL</span>
    <span class="brand-tagline">PAVEMENT SERVICES</span>
  </div>
  <span class="brand-square" aria-hidden="true"></span>
  <div class="footer-band" aria-hidden="true"></div>
</section>

</body>
</html>
```